RK Bastone Construction Inc.

Design a new business card for our construction company
To be removed from current card:
Delete 25 years
Delete Tenant fit up Renovations section

```html
<!DOCTYPE html>
<html lang="en">
<head>
<meta charset="utf-8">
<title>RK Bastone Construction Inc. — Business Card</title>
<link rel="stylesheet" href="https://fonts.googleapis.com/css2?family=Roboto:wght@300;400;500;700&display=swap">
<style>
  :root {
    --bg: #e6e6e8;
    --purple: #4f2a6c;
    --purple-light: #8a4fc6;
    --teal: #1f6f63;
    --white: #ffffff;
    --text-soft: #e9e0f2;
  }
  * { box-sizing: border-box; margin: 0; padding: 0; }
  html, body { width: 1200px; height: 796px; overflow: hidden; background: var(--bg); }
  body { font-family: "Roboto", Arial, sans-serif; position: relative; }

  .card {
    position: absolute;
    top: 243px;
    width: 540px;
    height: 310px;
    border-radius: 22px;
    overflow: hidden;
    box-shadow: 0 10px 28px rgba(0,0,0,0.18);
    border-bottom: 2px solid var(--teal);
  }
  .card--front { left: 40px; background: var(--purple); }
  .card--back { left: 620px; background: var(--purple); display: flex; align-items: center; justify-content: center; }

  .front__top {
    height: 138px;
    background: var(--white);
    display: flex;
    align-items: center;
    justify-content: center;
    border-bottom: 3px solid var(--teal);
  }
  .wordmark {
    font-weight: 700;
    font-size: 26px;
    letter-spacing: 0.5px;
    color: var(--purple);
    text-transform: uppercase;
    text-align: center;
    line-height: 1;
    white-space: nowrap;
  }
  .card--back .wordmark { color: var(--purple-light); }

  .front__bottom {
    display: flex;
    align-items: center;
    justify-content: center;
    height: 169px;
    color: var(--white);
    gap: 22px;
  }
  .person { text-align: right; font-size: 14px; line-height: 1.45; font-weight: 300; }
  .person__name { font-weight: 500; font-size: 17px; text-transform: uppercase; letter-spacing: 0.5px; }
  .divider { width: 1px; height: 92px; background: var(--text-soft); opacity: 0.7; }
  .contact { list-style: none; font-size: 13.5px; font-weight: 300; line-height: 1.6; }
  .contact li { display: flex; align-items: center; gap: 9px; }
  .contact svg { width: 12px; height: 12px; flex: none; fill: var(--white); }
</style>
</head>
<body>
  <section class="card card--front" aria-label="Business card front">
    <div class="front__top">
      <p class="wordmark">RK Bastone Construction Inc.</p>
    </div>
    <div class="front__bottom">
      <div class="person">
        <p class="person__name">Marco Bastone</p>
        <p>Managing Director</p>
        <p>1280 Orchard Rd, Suite 210</p>
        <p>Ottawa, ON K2P4R7</p>
      </div>
      <div class="divider"></div>
      <ul class="contact">
        <li><svg viewBox="0 0 12 12"><path d="M2.5 0.8l2 2.2-1.1 1.5c0.7 1.6 2 2.9 3.6 3.6l1.5-1.1 2.2 2-1.2 1.8C4.8 10.6 1.4 7.2 0.6 2z"/></svg>613-555-0142 ext.305</li>
        <li><svg viewBox="0 0 12 12"><path d="M3 0.5h6a1 1 0 0 1 1 1v9a1 1 0 0 1-1 1H3a1 1 0 0 1-1-1v-9a1 1 0 0 1 1-1zm0.6 1.4v7.4h4.8V1.9z"/></svg>613-555-0187</li>
        <li><svg viewBox="0 0 12 12"><path d="M0.5 2.5h11v7h-11zM1.5 3.5v0.4L6 6.8l4.5-2.9v-0.4z"/></svg>marco@rkbastoneconst.ca</li>
        <li><svg viewBox="0 0 12 12"><circle cx="6" cy="6" r="5.5"/></svg>www.rkbastoneconst.ca</li>
      </ul>
    </div>
  </section>

  <section class="card card--back" aria-label="Business card back">
    <p class="wordmark">RK Bastone Construction Inc.</p>
  </section>
</body>
</html>
```